Guitar teacher and Composer needs a Business Card design

I am looking for a designer who would like to implement the general idea of the design which I am providing with a draft in the uploaded file called Tomo.png. Please feel free to add your own creative touch to my idea.
There should definitely be an abstract image of a guitar on the business card. The colours to use - black and white, could be also grey. Which one to use as the main colour - to your decision. You can try to make it half-half, for example black part with guitar and the rest - white or the other way round. Would be cool to see there some element standing out in red, such as some note, or one or all strings of the guitar, or the line of the contour of the guitar for example..
It would also be nice to see a "reverse" version where the background would be black and the strings and contour of the guitar would be white etc.
Thanks to everyone who is going to participate in this design project!
Target Market(s)
potential students and customers
Industry/Entity Type
Teacher
Contact Information for Business Card
see "Project description"
Requirements
Must have
- I want to have an ABSTRACT image of a CLASSICAL guitar or part of it. It can be just the contour of it or just a few lines giving a hint about it or so.
Nice to have
- Would be good to have some small element standing out in red. Like some little detail, or one line, or icons of contacts, or string(s) of the guitar, or a note.......
Should not have
- I DON'T want to have a PHOTO of a guitar on my business card. And i DON'T need an image of an E-GUITAR.
- I don't want the words "Phone", "E-Mail", "Website", or "Address" to appear on the business card but rather have icons/symbols for that, as shown in my draft.

```html
<!DOCTYPE html>
<html lang="de">
<head>
<meta charset="utf-8">
<title>Mira Kovalenko – Visitenkarte</title>
<link href="https://fonts.googleapis.com/css2?family=Didact+Gothic&display=swap" rel="stylesheet">
<style>
  :root {
    --stage: #2a2a2a;
    --card-black: #000000;
    --accent-red: #e8222b;
    --paper-white: #ffffff;
    --muted-grey: #7a7a7a;
    --guitar-light: #f2f2f2;
    --guitar-shade: #cfcfcf;
  }
  html, body {
    margin: 0;
    width: 1200px;
    height: 800px;
    overflow: hidden;
    background: var(--stage);
    font-family: "Didact Gothic", "Helvetica Neue", Arial, sans-serif;
  }
  .business-card {
    position: absolute;
    left: 120px;
    top: 100px;
    width: 960px;
    height: 600px;
    background: var(--card-black);
    overflow: hidden;
  }
  .identity {
    position: absolute;
    left: 70px;
    top: 235px;
    width: 400px;
    color: var(--paper-white);
  }
  .identity__name {
    margin: 0;
    font-size: 34px;
    font-weight: 400;
    letter-spacing: 5px;
    text-transform: uppercase;
    white-space: nowrap;
  }
  .identity__roles {
    margin: 18px 0 0 8px;
    padding: 0;
    list-style: none;
    color: var(--muted-grey);
    font-size: 20px;
    letter-spacing: 2.5px;
    line-height: 1.4;
  }
  .divider {
    position: absolute;
    left: 495px;
    top: 150px;
    width: 2px;
    height: 240px;
    background: linear-gradient(to bottom, transparent, var(--accent-red) 50%, transparent);
    opacity: 0.7;
  }
  .contacts {
    position: absolute;
    right: 232px;
    top: 180px;
    margin: 0;
    padding: 0;
    list-style: none;
    text-align: right;
    color: var(--paper-white);
    font-size: 22px;
    letter-spacing: 1.5px;
    line-height: 48px;
    white-space: nowrap;
  }
  .contact-icons {
    position: absolute;
    left: 748px;
    top: 186px;
    display: flex;
    flex-direction: column;
    gap: 12px;
  }
  .contact-icon {
    width: 36px;
    height: 36px;
    background: var(--paper-white);
    display: flex;
    align-items: center;
    justify-content: center;
  }
  .guitar-artwork {
    position: absolute;
    left: 800px;
    top: 0;
    width: 160px;
    height: 600px;
    background: linear-gradient(to bottom, var(--guitar-light), var(--guitar-shade));
  }
  .address-band {
    position: absolute;
    left: 0;
    bottom: 0;
    width: 800px;
    height: 130px;
    background: var(--accent-red);
    display: flex;
    align-items: center;
    padding-left: 90px;
    box-sizing: border-box;
    color: var(--paper-white);
    font-size: 30px;
    letter-spacing: 1px;
  }
  .address-band svg { margin-right: 28px; }
</style>
</head>
<body>
  <article class="business-card">
    <div class="identity">
      <h1 class="identity__name">Mira Kovalenko</h1>
      <ul class="identity__roles">
        <li>Gitarrenlehrer</li>
        <li>Komponist</li>
        <li>Arrangeur</li>
      </ul>
    </div>

    <div class="divider"></div>

    <ul class="contacts">
      <li>+49 170 555 20318</li>
      <li>mira@saiten.studio</li>
      <li>www.saiten.studio</li>
    </ul>

    <div class="contact-icons">
      <span class="contact-icon">
        <svg width="22" height="22" viewBox="0 0 24 24" aria-label="Telefon"><path d="M6.6 2.5l3 3.2-1.8 2.2c1.2 2.6 3.4 4.8 6 6l2.2-1.8 3.2 3-2 3.2C11 18 6 13 5 4.5z" fill="#000"/></svg>
      </span>
      <span class="contact-icon">
        <svg width="24" height="20" viewBox="0 0 24 20" aria-label="E-Mail"><rect x="2" y="3" width="20" height="14" fill="none" stroke="#000" stroke-width="2"/><path d="M2 3l10 8 10-8M2 17l7-6M22 17l-7-6" fill="none" stroke="#000" stroke-width="1.6"/></svg>
      </span>
      <span class="contact-icon">
        <svg width="24" height="22" viewBox="0 0 24 22" aria-label="Webseite"><rect x="2" y="2" width="20" height="13" fill="none" stroke="#000" stroke-width="2.2"/><path d="M12 15v4M7 20h10" stroke="#000" stroke-width="2.2"/></svg>
      </span>
    </div>

    <div class="guitar-artwork" role="img" aria-label="Abstrakte weiße Silhouette einer klassischen Gitarre mit Kopf, Bünden und Korpus"></div>

    <footer class="address-band">
      <svg width="30" height="40" viewBox="0 0 30 40" aria-label="Adresse"><path d="M15 1C7 1 2 7 2 14c0 9 13 24 13 24s13-15 13-24C28 7 23 1 15 1z" fill="#fff"/><circle cx="15" cy="14" r="5" fill="#e8222b"/></svg>
      <span>Lindenweg 7, München, 80331</span>
    </footer>
  </article>
</body>
</html>
```